Equipment Supplier Brochure Needed

We need a professional one-page, front-and-back brochure for Tovrik, an equipment and parts supplier serving peanut shelling and processing facilities across the Southeast. This brochure will be used as a leave-behind with plant managers and procurement teams, so it must look clean, modern, and visually strong.

Front of brochure:

Tovrik logo and strong branding

Brief headline/summary of what Tovrik does

Product category overview listed on the front (high-level, clean layout)

Flat Screens (slot, round, herringbone, square, Style 1 & Style 2)

Sheller Grates

Ripple Screens

Sheller Bars

Eccentric Bearing Housings

Eccentric Shafts

Rebuilt Machines

Ducts

Sprockets

Rubber Gum Balls

Fiberglass

Wilmot Penn Reels

Elevator Buckets

Space for several product photos (we’ve uploaded images)

Clean industrial aesthetic

Back of brochure:

More detailed visual layout of products

Strong callout section showing companies we represent (logos included)

Optional short paragraph about Tovrik’s capabilities, history, or differentiators

Contact info section

Overall style:

Clean, modern, print-ready

Industrial yet polished

Balanced visual + text layout

Color palette aligned with Tovrik brand

Final files delivered as print-ready PDF (plus editable source file if available)

We’ve uploaded product imagery, partner logos, and reference materials. Please design multiple layout concepts if possible.

```html
<!DOCTYPE html>
<html lang="en">
<head>
<meta charset="utf-8">
<title>Tovrik – Replacement Parts for Peanut Processing Equipment</title>
<link href="https://fonts.googleapis.com/css2?family=Antonio:wght@600;700&family=Montserrat:wght@400;500;600;700;800&display=swap" rel="stylesheet">
<style>
:root{
  --blue:#1b4aa5;
  --tan:#dcc69c;
  --gold:#e8c47f;
  --ink:#141414;
  --white:#ffffff;
  --line:#c9c9c9;
  --stage:#e8e6e6;
  --partner:#7d7d7d;
}
*{box-sizing:border-box;margin:0;padding:0}
html,body{width:747px;height:1200px;overflow:hidden;background:var(--stage)}
body{font-family:"Montserrat",sans-serif;color:var(--ink)}

.page{position:absolute;left:166px;width:645px;height:908px;overflow:hidden;background:var(--white);
  transform:scale(.643);transform-origin:0 0;box-shadow:0 3px 10px rgba(0,0,0,.25)}
.page-front{top:10px}
.page-back{top:606px}
.abs{position:absolute}
ul{list-style:none}

/* check bullets */
.check li{position:relative}
.check li::before{content:"";position:absolute;left:0;border-radius:50%;background:var(--blue)}
.check li::after{content:"";position:absolute;border:solid var(--white);border-width:0 0 1.6px 1.6px;transform:rotate(-45deg)}

/* ---------- front ---------- */
.hero{left:0;top:0;width:645px;height:330px;background:var(--blue)}
.hero-photo{position:absolute;right:0;top:0;width:62%;height:100%;
  background:
    radial-gradient(ellipse at 70% 62%,#c98b4d 0%,rgba(201,139,77,0) 48%),
    radial-gradient(ellipse at 45% 25%,#9a9ca3 0%,rgba(154,156,163,0) 40%),
    linear-gradient(160deg,#5c6270 0%,#a67446 55%,#d19a5b 100%);
  -webkit-mask-image:linear-gradient(to right,transparent 0%,#000 40%);
  mask-image:linear-gradient(to right,transparent 0%,#000 40%)}
.brand-panel{position:absolute;left:0;top:0;width:510px;height:107px;background:var(--white);
  clip-path:polygon(0 0,100% 0,91% 100%,0 100%)}
.brand-name{position:absolute;left:37px;top:25px;font-weight:800;font-size:54px;letter-spacing:3px;
  color:var(--blue);line-height:1;text-transform:uppercase}
.tagline{left:34px;top:142px;color:var(--white);font-size:15px;font-weight:500}
.headline{left:34px;top:168px;color:var(--white);font-family:"Antonio",sans-serif;font-weight:700;
  font-size:43px;line-height:46px;text-transform:uppercase}
.headline .accent{color:var(--gold)}

.intro{left:30px;right:30px;top:340px;text-align:center;font-size:11.2px;line-height:15px}
.intro .lead{font-weight:500}
.intro p+p{margin-top:8px}

.section-title{display:flex;align-items:center;gap:10px;font-weight:700;font-size:17px;white-space:nowrap}
.section-title::after{content:"";flex:1;height:2px;background:var(--blue)}
.cat-title{left:34px;right:30px;top:446px}

.cat-col{top:480px;height:122px;font-size:14.5px;font-weight:500;line-height:21.5px}
.cat-col li{padding-left:17px}
.cat-col li::before{top:5px;width:11px;height:11px}
.cat-col li::after{left:3px;top:8px;width:5px;height:3px}
.cat-col-1{left:38px;width:178px}
.cat-col-2{left:218px;width:209px;padding-left:34px;border-left:1px solid var(--line)}
.cat-col-3{left:427px;width:190px;padding-left:28px;border-left:1px solid var(--line)}

.products{left:0;top:615px;width:645px;height:293px;background:var(--tan)}
.prod-title{left:33px;right:30px;top:624px}
.photo{top:655px;width:136px;height:143px;border:3px solid var(--blue);border-radius:10px}
.photo-1{left:34px;background:linear-gradient(135deg,#5a5f66,#c8cbd0 45%,#7b8088)}
.photo-2{left:181px;background:radial-gradient(circle at 50% 45%,#3c3f44 0 12%,#c3c5c9 13% 38%,#6f737a 70%)}
.photo-3{left:331px;background:linear-gradient(160deg,#4a4c50,#b9bbbe 50%,#6b6d70)}
.photo-4{left:479px;background:linear-gradient(180deg,#3e434a,#9ea2a8 50%,#5a5e64)}

.address{left:33px;top:868px;display:flex;align-items:center;gap:8px;font-size:11.2px;font-weight:500}
.address-back{left:34px;top:854px;align-items:flex-end}
.address-back .label{display:block;font-size:13px;font-weight:700;line-height:15px}

.contact{right:0;bottom:0;width:355px;height:78px;background:var(--blue);
  clip-path:polygon(20% 0,100% 0,100% 100%,0 100%);color:var(--white);text-align:right;padding:9px 30px 0 0}
.contact .name{font-weight:700;font-size:13.5px;line-height:16px}
.contact .email{font-size:13.5px;line-height:17px;color:var(--gold);display:flex;justify-content:flex-end;align-items:center;gap:7px}
.contact .phone{font-size:20px;line-height:26px;font-weight:700;color:var(--gold);display:flex;justify-content:flex-end;align-items:center;gap:7px}

/* ---------- back ---------- */
.about{left:0;top:0;width:645px;height:235px;background:var(--blue);color:var(--white)}
.about-col{position:absolute;top:22px;width:186px}
.about-col:nth-child(1){left:35px}
.about-col:nth-child(2){left:238px}
.about-col:nth-child(3){left:440px}
.about .kicker{font-size:11px;font-weight:500;line-height:12px}
.about h2{font-size:21px;font-weight:700;line-height:21px;text-transform:uppercase;margin-top:1px}
.about .spacer{height:12px}
.about p{font-size:9.4px;line-height:14.4px;margin-top:7px}

.group h3{font-size:17px;font-weight:700;text-transform:uppercase;line-height:20px}
.group ul{margin-top:7px;font-size:9.4px;line-height:14.4px;font-weight:500}
.group li{padding-left:13px}
.group li::before{top:4px;width:7px;height:7px}
.group li::after{left:2px;top:6px;width:3px;height:1.6px;border-width:0 0 1px 1px}
.g-ecc{left:34px;top:246px;width:200px}
.g-sheller{left:250px;top:246px;width:178px}
.g-screens{left:251px;top:340px;width:178px}
.g-deck{left:452px;top:246px;width:165px}

.tile{width:137px;height:125px;border:4px solid var(--tan)}
.r1{top:495px}.r2{top:631px}
.c1{left:37px}.c2{left:183px}.c3{left:330px}.c4{left:477px}
.t-a{background:linear-gradient(135deg,#4f4a43,#b9b2a6 50%,#6c655d)}
.t-b{background:linear-gradient(160deg,#7d8289,#d3d6da 50%,#8a8f96)}
.t-c{background:linear-gradient(90deg,#8b8f94,#c9ccd0 50%,#8b8f94)}
.t-d{background:radial-gradient(circle at 50% 40%,#efe6cf,#cbbd9b 60%,#3b3b3b)}
.t-e{background:linear-gradient(180deg,#8a5a3b,#c99874 50%,#6d452b)}
.t-f{background:linear-gradient(180deg,#c4c7cb,#80858c 55%,#5c6168)}
.t-g{background:linear-gradient(150deg,#d8c7a5,#bfa67b 55%,#e2d6bd)}
.t-h{background:linear-gradient(170deg,#d6d6d6,#3f4246 60%,#6b6e72)}

.partners{left:34px;top:768px;width:580px;height:42px;display:flex;align-items:center}
.partner{flex:1;display:flex;align-items:center;justify-content:center;gap:6px;font-size:15px;font-weight:600;color:var(--partner)}
.partner+.partner{border-left:1.5px solid var(--blue);height:38px}
.partner .mark{width:12px;height:12px;background:var(--partner)}
</style>
</head>
<body>

<!-- front side -->
<article class="page page-front">
  <header class="abs hero">
    <div class="hero-photo" role="img" aria-label="Photo of shelled peanuts moving along a processing line"></div>
    <div class="brand-panel"><div class="brand-name">Tovrik</div></div>
  </header>
  <p class="abs tagline">We Manufacture &amp; Supply</p>
  <h1 class="abs headline">Replacement parts for<br><span class="accent">Peanut</span> processing<br>equipment</h1>

  <section class="abs intro">
    <p class="lead">We believe in simple small town values like hard work, community and quality. That's why you'll find our team working day in and day out to provide our customers with quality products.</p>
    <p>Our replacement parts are designed and manufactured in our fabrication facility in Dothan, AL. With our American made parts, you can be assured of quality, availability and on-time delivery. Our parts are fabricated to exact customer specifications.</p>
  </section>

  <h2 class="abs section-title cat-title">Product category :</h2>
  <ul class="abs check cat-col cat-col-1">
    <li>Flat Screens</li><li>Sheller Grates</li><li>Ripple Screens</li><li>Sheller Bars</li><li>Eccentric Bearing Housings</li>
  </ul>
  <ul class="abs check cat-col cat-col-2">
    <li>Eccentric Shafts</li><li>Rebuilt Machines</li><li>Ducts</li><li>Sprockets</li>
  </ul>
  <ul class="abs check cat-col cat-col-3">
    <li>Rubber Gum Balls</li><li>Fiberglass</li><li>Wilmot Penn Reels</li><li>Elevator Buckets</li>
  </ul>

  <div class="abs products"></div>
  <h2 class="abs section-title prod-title">Several product :</h2>
  <div class="abs photo photo-1" role="img" aria-label="Photo of a ripple screen"></div>
  <div class="abs photo photo-2" role="img" aria-label="Photo of an eccentric bearing housing"></div>
  <div class="abs photo photo-3" role="img" aria-label="Photo of steel eccentric shafts"></div>
  <div class="abs photo photo-4" role="img" aria-label="Photo of stacked reel screens"></div>

  <div class="abs address">
    <svg width="16" height="20" viewBox="0 0 18 22"><path d="M9 1a6.5 6.5 0 0 0-6.5 6.5C2.5 12.5 9 18 9 18s6.5-5.5 6.5-10.5A6.5 6.5 0 0 0 9 1z" fill="none" stroke="#141414" stroke-width="2"/><circle cx="9" cy="7.5" r="2.3" fill="#141414"/><path d="M3 20.5h12" stroke="#141414" stroke-width="2"/></svg>
    <span>418 W Mill Street Dothan, AL 36301</span>
  </div>

  <footer class="abs contact">
    <p class="name">Dale Hutchins</p>
    <p class="email"><svg width="14" height="10" viewBox="0 0 16 12"><rect x="1" y="1" width="14" height="10" fill="none" stroke="#fff" stroke-width="1.5"/><path d="M1 1l7 6 7-6" fill="none" stroke="#fff" stroke-width="1.5"/></svg><span>Email : dale@tovrikinc.com</span></p>
    <p class="phone"><svg width="17" height="17" viewBox="0 0 20 20"><path d="M4 2l3 .5 1.2 3.8-2 1.5a10 10 0 0 0 6 6l1.5-2 3.8 1.2.5 3c-.2 1-1 1.8-2 1.8C9 17.8 2.2 11 2.2 4c0-1 .8-1.8 1.8-2z" fill="none" stroke="#fff" stroke-width="1.8"/></svg><span>(334) 555-0182</span></p>
  </footer>
</article>

<!-- back side -->
<article class="page page-back">
  <section class="abs about">
    <div class="about-col">
      <p class="kicker">OUR CAPABILITIES</p>
      <h2>What we do</h2>
      <p>At TOVRIK, Inc., we manufacture and distribute replacement parts for peanut processing equipment. American-made, high-quality parts that are designed to work great in your equipment. We have been producing, reliable products at our facility Dothan, Alabama since 1996.</p>
    </div>
    <div class="about-col">
      <div class="spacer"></div>
      <h2>Our story</h2>
      <p>Our replacement parts are designed and manufactured in our fabrication facility in Dothan, AL. With our American made parts, you can be assured of quality, availability and on-time delivery. Our parts are fabricated to exact customer specifications.</p>
    </div>
    <div class="about-col">
      <div class="spacer"></div>
      <h2>We support<br>agriculture</h2>
      <p>Agriculture is fundamental to both our lives and our economy. Southern peanut farmers face many challenges today as they work to supply worldwide demand. We are proud to play a role in the agricultural process, and we are committed to supporting America's peanut industry.</p>
    </div>
  </section>

  <section class="abs group g-ecc">
    <h3>Eccentrics</h3>
    <ul class="check">
      <li>Eccentric Bearings</li><li>Eccentric Cams</li><li>Eccentric Housings</li><li>Eccentric Rods</li>
      <li>Support Springs &amp; Connectors</li><li>Phenolic Pads</li><li>Drive Guards</li>
      <li>Ducts (Curtains for Separators, Stoners &amp; Shakers)</li><li>Shafting</li><li>Elevator Chains</li>
      <li>Sprockets</li><li>Clampwell Clamps</li><li>Gum Rubber Balls</li>
    </ul>
  </section>
  <section class="abs group g-sheller">
    <h3>Sheller parts</h3>
    <ul class="check">
      <li>Haverton Sheller Grates</li><li>Sheller Bars (Lead, Return, and Nub)</li><li>Sheller Hopper Boxes</li>
    </ul>
  </section>
  <section class="abs group g-screens">
    <h3>Screens</h3>
    <ul class="check">
      <li>Rippled Screens (Low &amp; High Profile for Separator and Stoner Decks)</li>
      <li>Perforated Flat Screens (Round and Slotted)</li><li>Screen Frames</li><li>Air Intake Filter Screens</li>
    </ul>
  </section>
  <section class="abs group g-deck">
    <h3>Deck parts</h3>
    <ul class="check">
      <li>Deck Cap Assemblies and Components</li><li>Food Grade Deck Sealant (Weather Stripping)</li><li>Misc Deck Components</li>
    </ul>
  </section>

  <div class="abs tile r1 c1 t-a" role="img" aria-label="Photo of screen frames stored on racks"></div>
  <div class="abs tile r1 c2 t-b" role="img" aria-label="Photo of a rippled screen surface"></div>
  <div class="abs tile r1 c3 t-c" role="img" aria-label="Photo of cylindrical reel screens"></div>
  <div class="abs tile r1 c4 t-d" role="img" aria-label="Photo of rubber gum balls"></div>
  <div class="abs tile r2 c1 t-e" role="img" aria-label="Photo of sheller bars"></div>
  <div class="abs tile r2 c2 t-f" role="img" aria-label="Photo of a machined eccentric shaft"></div>
  <div class="abs tile r2 c3 t-g" role="img" aria-label="Photo of a large sprocket"></div>
  <div class="abs tile r2 c4 t-h" role="img" aria-label="Photo of stacked sprockets"></div>

  <div class="abs partners">
    <div class="partner">Haverton</div>
    <div class="partner">Clampwell</div>
    <div class="partner">Unity Works</div>
    <div class="partner"><span class="mark"></span>Wilmot Penn</div>
  </div>

  <div class="abs address address-back">
    <svg width="16" height="20" viewBox="0 0 18 22"><path d="M9 1a6.5 6.5 0 0 0-6.5 6.5C2.5 12.5 9 18 9 18s6.5-5.5 6.5-10.5A6.5 6.5 0 0 0 9 1z" fill="none" stroke="#141414" stroke-width="2"/><circle cx="9" cy="7.5" r="2.3" fill="#141414"/><path d="M3 20.5h12" stroke="#141414" stroke-width="2"/></svg>
    <span><span class="label">Location</span>418 W Mill Street Dothan, AL 36301</span>
  </div>

  <footer class="abs contact">
    <p class="name">Dale Hutchins</p>
    <p class="email"><svg width="14" height="10" viewBox="0 0 16 12"><rect x="1" y="1" width="14" height="10" fill="none" stroke="#fff" stroke-width="1.5"/><path d="M1 1l7 6 7-6" fill="none" stroke="#fff" stroke-width="1.5"/></svg><span>Email : dale@tovrikinc.com</span></p>
    <p class="phone"><svg width="17" height="17" viewBox="0 0 20 20"><path d="M4 2l3 .5 1.2 3.8-2 1.5a10 10 0 0 0 6 6l1.5-2 3.8 1.2.5 3c-.2 1-1 1.8-2 1.8C9 17.8 2.2 11 2.2 4c0-1 .8-1.8 1.8-2z" fill="none" stroke="#fff" stroke-width="1.8"/></svg><span>(334) 555-0182</span></p>
  </footer>
</article>

</body>
</html>
```